Website Banners

I am working on a new website and need some banners for the main service pages. I will need 5 in total and may potentially choose from multi-designers and increase the payment or will choose the designer for all 5 based on the first one.

I am including a s the link to the development site. all the graphics in there at the moment are conceptual but give you an idea of what I am looking for.

___________________________

http://staging.brellowix.example/

On the home page I am looking for the main banner to represent an organisation moving or transitioning to the cloud but I want to use an individual (like a runner) to represent that.

I would like a text overlay for that banner to say: "Businesses don't transition themselves, so what are you waiting for?" or "Get ready for business at the speed of sound"

http://staging.brellowix.example/about-2/

On the About page I am looking for two banners. The first one to depict an Australian city street with a text overlay to say: "We stand for mid-market Australia". The second one to depict a local government/council image with a text overlay to say "We are local government and public sector experts"

http://staging.brellowix.example/about-2

On the Advisory page I am looking for a banner that depicts "trust" in a professional business sense with a text overlay to say "Challenge yourself - or have us do it for you"

http://staging.brellowix.example/consulting/

On the Consulting page I am looking for two banners. The first one to depict "getting your hands dirty" or "getting in there and getting the job done" with a text overlay to say "If you want success in your business put us there". The second one with an image to depict a competitive consulting environment with a text overlay to say "We understand we are an option but our approach is to make you a priority"

5 all up. I don't care which one you respond to.

My logo is attached.

I have also attached a couple of other designs that I have gone for in the past.

Target Market(s)

mid market (sized) businesses

Industry/Entity Type

It Service

Font styles to use
Serif

Colors
33a6d7
3176b4
f68d4d
f37122
ffffff

Requirements
Must have
• energy

```html
<!DOCTYPE html>
<html lang="en">
<head>
<meta charset="utf-8">
<title>Brellowix Advisory – Transition Banner</title>
<link rel="stylesheet" href="https://fonts.googleapis.com/css2?family=Exo+2:wght@400;700&display=swap">
<style>
  :root {
    --canvas: #ffffff;
    --frame: #8a8a8a;
    --ink: #333333;
    --accent-blue: #3f5fa8;
    --band-end: #7b8ec6;
    --runner-dark: #14233a;
    --runner-mid: #1f6fae;
    --panel-light: #f4f5f6;
    --panel-dark: #d9dcdf;
    --ring-outer: #e3e5e8;
    --ring-teal: #16607f;
    --dot-light: #2aa0d8;
    --dot-dark: #0f6ea6;
    --brand: #3a4fa0;
  }
  html, body {
    margin: 0;
    padding: 0;
    overflow: hidden;
    background: var(--canvas);
  }
  .banner {
    position: relative;
    width: 1200px;
    height: 514px;
    box-sizing: border-box;
    border: 1px solid var(--frame);
    background: var(--canvas);
    overflow: hidden;
    font-family: "Exo 2", sans-serif;
  }
  .runner-photo {
    position: absolute;
    left: 75px;
    top: 28px;
    width: 510px;
    height: 456px;
    border-radius: 40% 35% 30% 45%;
    background: radial-gradient(ellipse at 55% 40%, var(--runner-mid) 0%, var(--runner-dark) 70%, rgba(20,35,58,0) 100%);
    opacity: 0.85;
  }
  .headline-band {
    position: absolute;
    left: 605px;
    top: 52px;
    width: 595px;
    height: 163px;
    background: linear-gradient(90deg, rgba(255,255,255,1) 0%, var(--band-end) 100%);
  }
  .headline {
    position: absolute;
    right: 88px;
    top: 66px;
    margin: 0;
    text-align: right;
    color: var(--ink);
    font-size: 32px;
    font-weight: 400;
    line-height: 45px;
  }
  .headline .lead { font-weight: 700; }
  .headline .highlight { color: var(--accent-blue); }
  .brand-panel {
    position: absolute;
    left: 513px;
    top: 318px;
    width: 500px;
    height: 100px;
    border-radius: 6px;
    background: linear-gradient(180deg, var(--panel-light) 0%, var(--panel-dark) 100%);
    box-shadow: 0 2px 6px rgba(0,0,0,0.15);
    display: flex;
    align-items: center;
    padding-left: 38px;
    box-sizing: border-box;
  }
  .brand-name {
    color: var(--brand);
    font-size: 34px;
    font-weight: 400;
    letter-spacing: 1px;
  }
  .brand-dot {
    position: absolute;
    left: 938px;
    top: 260px;
    width: 200px;
    height: 200px;
  }
</style>
</head>
<body>
  <div class="banner">
    <div class="runner-photo" role="img" aria-label="Photo of a sprinter in a blue shirt bursting off the starting blocks"></div>

    <div class="headline-band"></div>
    <p class="headline">
      <span class="lead">Businesses</span><br>
      don't transition <span class="highlight">themselves</span><br>
      so what are you waiting for?
    </p>

    <div class="brand-panel">
      <span class="brand-name">BRELLOWIX ADVISORY</span>
    </div>

    <svg class="brand-dot" viewBox="0 0 200 200" aria-hidden="true">
      <defs>
        <radialGradient id="dot-fill" cx="40%" cy="40%" r="65%">
          <stop offset="0%" stop-color="var(--dot-light)"/>
          <stop offset="100%" stop-color="var(--dot-dark)"/>
        </radialGradient>
      </defs>
      <circle cx="100" cy="100" r="98" fill="var(--ring-outer)"/>
      <circle cx="100" cy="100" r="80" fill="var(--ring-teal)"/>
      <circle cx="100" cy="100" r="70" fill="#ffffff"/>
      <circle cx="100" cy="100" r="60" fill="url(#dot-fill)"/>
    </svg>
  </div>
</body>
</html>
```